The homepage of a website

This is a simple project that should take from you a few minutes as what is needed is the design of the homepage only, the details are in the attached zip file

Please note that KBLTA board required a special tailored design where they got some parts from the different posted designs, if you are interested please follow the instructions in the below URL and submit your new updated designs as per the instructions (P.S. I will mark the project as guaranteed as an assurance to all of you)

http://quorvanet.com/Projects/KBLTA/Design.jpg

Please note that KBLTA board required a special tailored design where they got some parts from the different posted designs, if you are interested please follow the instructions in the below URL and submit your new updated designs as per the instructions (P.S. I will mark the project as guaranteed as an assurance to all of you) http://quorvanet.com/Projects/KBLTA/Design.jpg

```html
<!DOCTYPE html>
<html lang="en">
<head>
<meta charset="utf-8">
<title>KBLTA — Home</title>
<link rel="stylesheet" href="https://fonts.googleapis.com/css2?family=Open+Sans:wght@400;600&display=swap">
<style>
:root{
  --blue:#2a6db0;
  --blue-dark:#1d5a98;
  --nav-top:#3d86cc;
  --nav-bottom:#1f5e9e;
  --orange:#f05a22;
  --text:#555;
  --dark:#333;
  --rule:#cfcfcf;
  --footer-bg:#efefef;
  --bottom-bg:#2b2b2b;
}
*{margin:0;padding:0;box-sizing:border-box}
html,body{width:706px;height:1200px;overflow:hidden}
body{font-family:"Open Sans",Arial,sans-serif;color:var(--text);background:#fff;position:relative}
.abs{position:absolute}
.topline{left:0;top:0;width:706px;height:3px;background:var(--blue-dark)}
.brand-mark{left:38px;top:22px;width:80px;height:80px;border-radius:50%;background:#e4edf6}
.brand-name{left:132px;top:26px;width:200px;color:var(--blue-dark);font-weight:600}
.brand-name .short{font-size:26px;line-height:30px;letter-spacing:2px}
.brand-name .long{font-size:10px;line-height:13px;margin-top:6px}
.lang{left:616px;top:41px;font-size:7.5px;color:var(--dark)}
.account{left:357px;top:92px;font-size:7.5px;color:var(--blue-dark)}
.login{left:449px;top:83px;width:67px;height:17px;background:var(--orange);color:#fff;font-size:7.5px;text-align:center;line-height:17px;border-radius:2px}
.forgot{left:449px;top:104px;font-size:6.5px;color:var(--dark);text-decoration:underline}
.search{left:532px;top:72px;width:138px;height:28px;border:1px solid #ccc;border-radius:2px;font-size:8px;color:var(--dark);display:flex;align-items:center;padding-left:10px;gap:6px}
.nav{left:0;top:122px;width:706px;height:28px;background:linear-gradient(var(--nav-top),var(--nav-bottom));display:flex;align-items:center;padding-left:34px;gap:21px;font-size:7.5px;color:#fff}
.hero{left:0;top:150px;width:706px;height:230px;background:linear-gradient(180deg,#9a8f86 0%,#d8a867 45%,#c9954f 100%)}
.hero-card{left:35px;top:192px;width:199px;height:124px;background:rgba(110,110,110,.6);color:#fff;padding:20px 18px}
.hero-card h1{font-weight:400;font-size:16px;line-height:20px}
.hero-card p{font-size:7px;line-height:9px;margin-top:14px;color:#eee}
.dots{left:338px;top:364px;display:flex;gap:5px}
.dots i{width:5px;height:5px;border-radius:50%;background:#222}
.dots i.on{background:var(--blue)}
.about-title{left:35px;top:396px;font-size:16px;color:var(--blue);font-weight:400}
.about-text{left:35px;top:426px;width:440px;font-size:7.5px;line-height:13px;color:var(--text)}
.btn{background:var(--orange);color:#fff;font-size:7.5px;text-align:center;border-radius:2px;box-shadow:0 1px 2px rgba(0,0,0,.3)}
.read{left:35px;top:486px;width:56px;height:22px;line-height:22px}
.calendar{left:500px;top:400px;width:172px;height:104px;background:linear-gradient(#f7f7f7,#e6e6e6);box-shadow:0 2px 5px rgba(0,0,0,.2)}
.rule{left:35px;width:635px;height:1px;background:var(--rule)}
.feature{top:572px;width:150px;text-align:center}
.feature svg{display:block;margin:0 auto}
.feature h3{font-size:12px;font-weight:400;color:var(--blue);margin-top:8px}
.feature p{font-size:7.5px;line-height:13px;margin-top:6px}
.sec-title{top:742px;font-size:13px;color:var(--blue);font-weight:400;display:flex;align-items:center;gap:7px}
.thumb{position:absolute}
.ev-img{left:35px;width:90px;height:76px}
.ev{left:134px;width:112px}
.ev h4{font-size:10.5px;font-weight:400;color:var(--dark);line-height:12px}
.ev .date{font-size:6.5px;color:#888;margin:6px 0 4px}
.ev p{font-size:7.5px;line-height:13px}
.gal{width:63px;height:52px}
.journal{left:494px;top:775px;width:180px}
.journal h4{font-size:10.5px;font-weight:400;color:var(--dark)}
.journal .date{font-size:6.5px;color:#555;margin:3px 0 6px}
.journal p{font-size:7.5px;line-height:13px}
.details{left:494px;top:926px;width:63px;height:27px;line-height:27px}
.footer{left:0;top:994px;width:706px;height:158px;background:var(--footer-bg)}
.f-title{top:1022px;font-size:13px;color:var(--dark);display:flex;align-items:center;gap:7px}
.f-col{top:1054px;font-size:7.5px;line-height:13px;color:var(--text)}
.f-col ul{list-style:none}
.f-col li::before{content:"•";margin-right:6px}
.mail-box{left:167px;top:1086px;width:155px;height:34px;border:1px solid #ccc;background:#fff;font-size:8.5px;color:#666;display:flex;align-items:center;justify-content:space-between;padding:0 8px}
.bottom{left:0;top:1152px;width:706px;height:48px;background:var(--bottom-bg)}
.copy{left:34px;top:1167px;font-size:7.5px;color:#bbb}
.social{top:1167px;width:12px;height:12px;border-radius:50%;background:#888}
</style>
</head>
<body>
<div class="abs topline"></div>

<header>
  <div class="abs brand-mark"></div>
  <div class="abs brand-name">
    <div class="short">KBLTA</div>
    <div class="long">The Karnak Board of Plastic &amp; Reconstructive Surgeons</div>
  </div>
  <div class="abs lang">English &nbsp;|&nbsp; Arabic</div>
  <div class="abs account">REGISTER | &nbsp;ACCOUNT</div>
  <div class="abs login">MEMBER LOGIN</div>
  <div class="abs forgot">Forgetpassword</div>
  <div class="abs search">
    <svg width="9" height="9" viewBox="0 0 10 10"><circle cx="4" cy="4" r="3" fill="none" stroke="#222" stroke-width="1.5"/><line x1="6.2" y1="6.2" x2="9" y2="9" stroke="#222" stroke-width="1.6"/></svg>
    Search
  </div>
</header>

<nav class="abs nav">
  <span>Home</span><span>Board</span><span>History</span><span>Members</span><span>Activities</span><span>Laws</span><span>Journal</span><span>Downloads</span><span>Board</span><span>Links</span><span>Contact</span>
</nav>

<section>
  <div class="abs hero" role="img" aria-label="Desert pyramid at sunset with a decorated camel in the foreground"></div>
  <div class="abs hero-card">
    <h1>The primary goal of the Karnak Board</h1>
    <p>advance the quality of care and safety of plastic surgery patients by demanding the highest standards in our members</p>
  </div>
  <div class="abs dots"><i></i><i class="on"></i><i></i></div>
</section>

<section>
  <h2 class="abs about-title">ABOUT KBLTA</h2>
  <p class="abs about-text">Nemo enim ipsam voluptatem quia voluptas sit aspernatur aut odit aut fugit, sed quia consequuntur magni dolores eos qui ratione voluptatem sequi nesciunt. Neque porro quisquam est,<br>qui dolorem ipsum quia dolor sit amet, consectetur, adipisci velit, sed quia non numquam eius modi tempora incidunt ut labore et dolore magnam aliquam quaerat voluptatem.</p>
  <div class="abs btn read">Read More</div>
  <div class="abs calendar" role="img" aria-label="Paper wall calendar page with a blue pin and a circled date"></div>
</section>

<div class="abs rule" style="top:540px"></div>

<section>
  <div class="abs feature" style="left:25px">
    <svg width="22" height="18" viewBox="0 0 22 18" fill="var(--blue)"><circle cx="11" cy="5" r="4"/><circle cx="4" cy="6" r="3"/><circle cx="18" cy="6" r="3"/><path d="M4 18c0-5 3-8 7-8s7 3 7 8z"/><path d="M0 16c0-4 2-6 4-6s3 1 3 1L5 16z"/><path d="M22 16c0-4-2-6-4-6s-3 1-3 1l2 5z"/></svg>
    <h3>Members pages</h3>
    <p>Nemo enim ipsam voluptatem quia voluptas sit aspernatur aut odit aut fugit, sed quia</p>
  </div>
  <div class="abs feature" style="left:182px">
    <svg width="22" height="18" viewBox="0 0 22 18" fill="var(--blue)"><path d="M11 0 22 5H0z"/><rect x="1" y="6" width="20" height="1.5"/><rect x="3" y="8" width="2.5" height="7"/><rect x="7.5" y="8" width="2.5" height="7"/><rect x="12" y="8" width="2.5" height="7"/><rect x="16.5" y="8" width="2.5" height="7"/><rect x="0" y="16" width="22" height="2"/></svg>
    <h3>Laws &amp; Regulations</h3>
    <p>Nemo enim ipsam voluptatem quia voluptas sit aspernatur aut odit aut fugit, sed quia</p>
  </div>
  <div class="abs feature" style="left:360px">
    <svg width="18" height="18" viewBox="0 0 18 18" fill="none" stroke="var(--blue)" stroke-width="1.8"><path d="M3 1v5a4 4 0 0 0 8 0V1"/><path d="M7 10v3a4 4 0 0 0 8 0v-4"/><circle cx="15" cy="7" r="1.8"/></svg>
    <h3>Patients education</h3>
    <p>Nemo enim ipsam voluptatem quia voluptas sit aspernatur aut odit aut fugit, sed quia</p>
  </div>
  <div class="abs feature" style="left:533px">
    <svg width="20" height="18" viewBox="0 0 20 18" fill="var(--blue)"><path d="M5 0h10v6a5 5 0 0 1-10 0z"/><path d="M5 2H1c0 4 2 6 4 6M15 2h4c0 4-2 6-4 6" fill="none" stroke="var(--blue)" stroke-width="1.5"/><rect x="9" y="10" width="2" height="4"/><rect x="5" y="14" width="10" height="3"/></svg>
    <h3>Universities</h3>
    <p>Nemo enim ipsam voluptatem quia voluptas sit aspernatur aut odit aut fugit, sed quia</p>
  </div>
</section>

<div class="abs rule" style="top:701px"></div>

<section>
  <h2 class="abs sec-title" style="left:35px">
    <svg width="12" height="12" viewBox="0 0 12 12" fill="none" stroke="var(--blue)" stroke-width="1.3"><rect x="1" y="2" width="10" height="9"/><line x1="1" y1="5" x2="11" y2="5"/><line x1="4" y1="0" x2="4" y2="3"/><line x1="8" y1="0" x2="8" y2="3"/></svg>
    EVENTS &amp; UPCOMING EVENTS
  </h2>
  <div class="thumb ev-img" style="top:778px;background:linear-gradient(135deg,#8fb2cc,#3f6f8f)" role="img" aria-label="Surgical team operating under theatre lights"></div>
  <div class="abs ev" style="top:777px">
    <h4>Lorem ipsum dolor sit amet</h4>
    <div class="date">posted by 03 Jan 2015</div>
    <p>Nemo enim ipsam voluptatem quia voluptas sit aspernatur aut odit aut fugit,</p>
  </div>
  <div class="thumb ev-img" style="top:878px;background:linear-gradient(135deg,#a9d6ee,#3d95c8)" role="img" aria-label="Surgeons in blue gowns during an operation"></div>
  <div class="abs ev" style="top:876px">
    <h4>Lorem ipsum dolor sit amet</h4>
    <div class="date">posted by 03 Jan 2015</div>
    <p>Nemo enim ipsam voluptatem quia voluptas sit aspernatur aut odit aut fugit,</p>
  </div>

  <h2 class="abs sec-title" style="left:268px">
    <svg width="13" height="11" viewBox="0 0 13 11" fill="none" stroke="var(--blue)" stroke-width="1.3"><rect x="1" y="1" width="11" height="9"/><path d="M2 9l3-4 3 3 2-2 2 3" /><circle cx="4" cy="3.5" r="1"/></svg>
    GALLERY
  </h2>
  <div class="thumb gal" style="left:269px;top:776px;background:linear-gradient(#e8eef4,#b9c9d8)" role="img" aria-label="Smiling doctor with stethoscope"></div>
  <div class="thumb gal" style="left:341px;top:776px;background:linear-gradient(#dbe8f6,#3f7fc4)" role="img" aria-label="Nurse in blue scrubs"></div>
  <div class="thumb gal" style="left:412px;top:776px;background:linear-gradient(#5b8ca6,#2e5366)" role="img" aria-label="Surgeons wearing masks"></div>
  <div class="thumb gal" style="left:269px;top:838px;background:linear-gradient(#9a9a9a,#3a3a3a)" role="img" aria-label="Clasped hands in black and white"></div>
  <div class="thumb gal" style="left:341px;top:838px;background:linear-gradient(#8a6f55,#3b2d22)" role="img" aria-label="Care home room with a patient"></div>
  <div class="thumb gal" style="left:412px;top:838px;background:linear-gradient(#b9d3ee,#8aa06a)" role="img" aria-label="Elderly couple walking outdoors"></div>
  <div class="thumb gal" style="left:269px;top:898px;background:linear-gradient(#8fb6de 45%,#c89a5a 46%)" role="img" aria-label="Pyramids under a blue sky"></div>
  <div class="thumb gal" style="left:341px;top:898px;background:linear-gradient(#4f95d8 30%,#d9a148 31%)" role="img" aria-label="Close view of a stepped pyramid"></div>
  <div class="thumb gal" style="left:412px;top:898px;background:linear-gradient(#5b93d4 45%,#c79b5c 46%)" role="img" aria-label="Sphinx with pyramid behind"></div>

  <h2 class="abs sec-title" style="left:496px">
    <svg width="13" height="11" viewBox="0 0 13 11" fill="var(--blue)"><path d="M1 10C2 4 6 1 13 1c-1 6-5 9-10 8z"/></svg>
    KBLTA JOURNAL
  </h2>
  <div class="abs journal">
    <h4>Publishing Information</h4>
    <div class="date">Posted by Jan 2015</div>
    <p>Nemo enim ipsam voluptatem quia voluptas sit aspernatur aut odit aut fugit, sed quia consequuntur magni dolores eos qui ratione voluptatem sequi nesciunt. Neque porro quisquam est, qui dolorem ipsum quia dolor sit amet, consectetur, adipisci velit, sed quia non numquam eius modi tempora incidunt ut labore et dolore magnam aliquam quaerat voluptatem.</p>
  </div>
  <div class="abs btn details">View Details</div>
</section>

<footer>
  <div class="abs footer"></div>
  <h2 class="abs f-title" style="left:36px">
    <svg width="11" height="11" viewBox="0 0 11 11" fill="none" stroke="var(--dark)" stroke-width="1.6"><path d="M4.5 6.5l2-2M3 5L1.5 6.5a2 2 0 0 0 3 3L6 8M8 6l1.5-1.5a2 2 0 0 0-3-3L5 3"/></svg>
    QUICK LINKS
  </h2>
  <div class="abs f-col" style="left:36px;width:130px">
    <ul><li>Scientific activities</li><li>Universities</li><li>E-Learning information</li><li>Research information</li><li>History of plastic surgery</li></ul>
  </div>

  <h2 class="abs f-title" style="left:167px">
    <svg width="13" height="10" viewBox="0 0 13 10" fill="var(--dark)"><rect width="13" height="10" rx="1"/><path d="M1 1l5.5 4.5L12 1" fill="none" stroke="#efefef" stroke-width="1.2"/></svg>
    NEWSLETTER
  </h2>
  <div class="abs f-col" style="left:167px;width:160px;line-height:10px">Nemo enim ipsam voluptatem quia voluptas sit aspernatur aut odit aut</div>
  <div class="abs mail-box">Enter Your Mail Id
    <svg width="10" height="10" viewBox="0 0 10 10"><circle cx="5" cy="5" r="4.3" fill="none" stroke="#333" stroke-width="1.1"/><path d="M2.8 5h4M5 3l2 2-2 2" fill="none" stroke="#333" stroke-width="1.1"/></svg>
  </div>

  <h2 class="abs f-title" style="left:344px">
    <svg width="11" height="11" viewBox="0 0 11 11"><rect width="11" height="11" rx="2" fill="var(--dark)"/><path d="M3 2.5c0 3 2.5 5.5 5.5 5.5l.5-1.5-1.5-.8-.8.8C5.5 6 5 5.5 4.5 4.3l.8-.8L4.5 2z" fill="#efefef"/></svg>
    &nbsp;CONTACT US
  </h2>
  <div class="abs f-col" style="left:344px;width:135px;line-height:10px">Nemo enim ipsam voluptatem quia voluptas sit</div>
  <div class="abs f-col" style="left:344px;top:1084px">1800-123-456</div>
  <div class="abs f-col" style="left:344px;top:1102px;color:var(--blue-dark);text-decoration:underline">info@yourMailId.com</div>

  <h2 class="abs f-title" style="left:500px">
    <svg width="10" height="11" viewBox="0 0 10 11" fill="var(--dark)"><circle cx="5" cy="3" r="3"/><path d="M0 11c0-4 2-5 5-5s5 1 5 5z"/></svg>
    &nbsp;TERMS OF MEMBERSHIP
  </h2>
  <div class="abs f-col" style="left:500px;top:1058px;width:175px">Nemo enim ipsam voluptatem quia voluptas sit aspernatur aut odit aut fugit, sed quia consequuntur magni dolores eos qui ratione voluptatem sequi nesciunt.</div>

  <div class="abs bottom"></div>
  <div class="abs copy">© 2015 kblta.com. All rights reserved.</div>
  <div class="abs social" style="left:608px"></div>
  <div class="abs social" style="left:630px"></div>
  <div class="abs social" style="left:658px"></div>
</footer>
</body>
</html>
```